Manuka honey jar label for new Manuka brand

We are planning to start a Manuka honey brand and we need to design the label for the honey jar. Manuka honey is an up and coming product and the market is still young in our country.
Our market is dominated by 1 brand: Orvana Health (photo attached). To the people who know what Manuka honey is, they associate it with Orvana Health in the same way people associate Cola with Zindle Pop or printer copies with Quorvix.
The good news is that a lot of people do not know yet what Manuka honey is and we still have the opportunity of being the first brand they get to know. At the same time, we still need to be able to take at least a bite out of the Orvana Health market share.
The Orvana Health label for their jar I think is not just absolutely gorgeous but it also does its job extremely well. It only features 3 informations:
- name of brand/logo (Orvana Health)
- name of product (Manuka Honey)
- and mgo rating which is like a rating of how strong the honey is
By having just this information on a relatively small label, their label SCREAMS Manuka by having the Manuka words twice (the brand and the product name) and people develop this association between Orvana Health and Manuka products in general.
Our product will also be in a similar square plastic jar. It will also be dark tinted, that´s important to note. We can also go for a blue cap but in order to differentiate ourselves from Orvana Health we thought of maybe choosing a black lid instead. I uploaded 2 jars, 1 with black lid and 1 with gold (although it looks more like mustard) that you can use for simulations. They are pretty accurate of the type of jars and lids that we can have.
The label has total length of about 20cm. One side of the jar has 5,5 cm of the label and the height of the label is 4,5 cm. We can also use selective gold laminating on the label but we cannot have custom shape label at this point as Orvana Health does with its tree logo that sticks outside the label.
I need the design for the entire label but the focus should be on the front part, that is the part that sells and catches your eye. Like Orvana Health, the front part I want to have 3 vital informations:
- name of brand/logo (in our case Velmora Botanica) - we do not have a pre-existing logo, this needs to be created alongside the label
- and mgo rating
As "other" information we also need the net weight "250 g" alongside with the typical "e" to appear on the front. That is a legal requirement.
Optionally, you can add a small phrase somewhere like "Harvested in New Zealand" or "Made in New Zealand" since this is a product that is only made there and in some areas of Australia.
This is pretty much all the info. As a final note, there are a ton of beautiful premium Manuka honey jar labels. But they are too fancy and when you look at them you don´t instantly recognize that it is Manuka Honey.
This instant recognition is vital! With this small jar there is the danger for customers to think that maybe it´s medicine, maybe it´s sports supplements etc. This is a relatively small product and imagine you just glance on it on the retail shelf. Instantly you must think it is Manuka Honey and that it is beautiful. And if you see it on the shelf next to Orvana Health, it would be best to also think that you would rather buy this (it gives you more trust) than the Orvana Health.
One final note: I do not want the bee as an insect on the label. I think some people are turned off when they see an insect with its small legs and make a bad association that there are insects inside. I do not mind symbolism or somehow super stylized bee in a modern way, but I do not want a plain insect on the label.
For any other questions, I am at your disposal. Thank you very much for taking the time to send us a proposal!

```html
<!DOCTYPE html>
<html lang="en">
<head>
<meta charset="utf-8">
<title>Velmora Botanica – Manuka Honey Jar Labels</title>
<link rel="stylesheet" href="https://fonts.googleapis.com/css2?family=Cinzel:wght@400;700&family=Montserrat:wght@400&family=Roboto+Condensed:wght@500&display=swap">
<style>
  :root {
    --page: #ffffff;
    --cream: #e9e6d6;
    --cream-pattern: #e4e0cf;
    --ink: #111111;
    --black: #050505;
    --black-pattern: #0d0d0c;
    --gold-dark: #b8750c;
    --gold-mid: #dca63e;
    --gold-light: #f5d37a;
    --white: #ffffff;
  }
  * { margin: 0; padding: 0; box-sizing: border-box; }
  html, body { width: 1200px; height: 1200px; overflow: hidden; background: var(--page); }
  .canvas { position: relative; width: 1200px; height: 1200px; }

  .label { position: absolute; left: 58px; width: 1084px; height: 244px; overflow: hidden; }
  .label--light { top: 322px; background: var(--cream); }
  .label--dark { top: 634px; background: var(--black); }

  .gold-gradient {
    background: linear-gradient(90deg, var(--gold-dark) 0%, var(--gold-mid) 25%, var(--gold-light) 50%, var(--gold-mid) 75%, var(--gold-dark) 100%);
  }

  .pattern { position: absolute; }
  .label--light .pattern { left: 77px; top: 6px; width: 928px; height: 220px; background: var(--cream-pattern); }
  .label--dark .pattern-field { left: 0; top: 33px; width: 1084px; height: 184px; background: var(--black-pattern); }
  .label--dark .pattern-comb { left: 83px; width: 920px; height: 27px; background: linear-gradient(180deg, #0b0a07, #14110a); }
  .pattern-comb--top { top: 0; }
  .pattern-comb--bottom { top: 222px; }

  .bar-top { position: absolute; left: 0; top: 0; width: 100%; height: 6px; }
  .bar-bottom { position: absolute; left: 0; top: 226px; width: 100%; height: 18px;
    display: flex; align-items: center; justify-content: center; }

  .rule { position: absolute; height: 3px; }
  .rule--top-left { left: 0; top: 30px; width: 504px; }
  .rule--top-right { left: 576px; top: 30px; width: 508px; }
  .rule--bottom { left: 0; top: 217px; width: 100%; }

  .net-weight {
    font-family: "Roboto Condensed", "Arial Narrow", sans-serif;
    font-weight: 500; font-size: 9px; letter-spacing: 0.1px;
  }
  .label--light .net-weight { color: var(--ink); }
  .label--dark .net-weight { position: absolute; left: 0; width: 100%; top: 226px; text-align: center; color: var(--white); }

  .brand-dot { position: absolute; border-radius: 50%; }
  .label--light .brand-dot { left: 511px; top: 13px; width: 62px; height: 62px; background: var(--ink); box-shadow: 0 0 0 1px var(--cream), 0 0 0 2px var(--ink); }
  .label--dark .brand-dot { left: 516px; top: 13px; width: 52px; height: 52px;
    background: radial-gradient(circle at 40% 35%, var(--gold-light), var(--gold-mid) 55%, var(--gold-dark)); }

  .brand-name {
    position: absolute; left: 0; width: 100%; text-align: center;
    font-family: "Cinzel", "Times New Roman", serif; font-weight: 400;
    font-size: 24px; line-height: 30px; letter-spacing: 1px;
  }
  .label--light .brand-name { top: 80px; color: var(--ink); }
  .label--dark .brand-name { top: 74px; color: var(--gold-mid); }

  .product-name {
    position: absolute; text-align: center;
    font-family: "Cinzel", "Times New Roman", serif; font-weight: 700;
    font-size: 27px; line-height: 27px; letter-spacing: 0.5px;
  }
  .label--light .product-name { left: 420px; width: 128px; top: 165px; color: var(--ink); }
  .label--dark .product-name { left: 432px; width: 120px; top: 160px; color: var(--white); }

  .grade-badge { position: absolute; }
  .label--light .grade-badge { left: 585px; top: 169px; width: 54px; height: 33px; }
  .label--dark .grade-badge { left: 575px; top: 164px; width: 46px; height: 29px; }

  .origin {
    position: absolute; font-family: "Montserrat", Arial, sans-serif;
    font-size: 7px; letter-spacing: 0.2px; white-space: nowrap;
  }
  .label--light .origin { left: 561px; top: 207px; color: #333; }
  .label--dark .origin { left: 547px; top: 200px; color: #cfcfcf; }
</style>
</head>
<body>
<main class="canvas">

  <section class="label label--light" aria-label="Cream label variant">
    <div class="pattern" role="img" aria-label="Faint geometric line pattern on cream ground"></div>
    <div class="bar-top gold-gradient"></div>
    <div class="brand-dot"></div>
    <h1 class="brand-name">VELMORA<br>BOTANICA</h1>
    <h2 class="product-name">MANUKA<br>HONEY</h2>
    <svg class="grade-badge" viewBox="0 0 54 33" aria-label="Grade rating badge">
      <polygon points="8,1 46,1 53,16.5 46,32 8,32 1,16.5" fill="none" stroke="#111" stroke-width="1.5"/>
      <polygon points="10,4 44,4 50,16.5 44,29 10,29 4,16.5" fill="none" stroke="#111" stroke-width="0.8"/>
    </svg>
    <p class="origin">HARVESTED IN NEW ZEALAND</p>
    <div class="bar-bottom gold-gradient"><span class="net-weight">250g (8.8oz) NET Wt.</span></div>
  </section>

  <section class="label label--dark" aria-label="Black label variant">
    <div class="pattern pattern-field" role="img" aria-label="Fine diagonal line texture on black ground"></div>
    <div class="pattern pattern-comb pattern-comb--top" role="img" aria-label="Dark honeycomb pattern band"></div>
    <div class="pattern pattern-comb pattern-comb--bottom" role="img" aria-label="Dark honeycomb pattern band"></div>
    <div class="rule rule--top-left gold-gradient"></div>
    <div class="rule rule--top-right gold-gradient"></div>
    <div class="rule rule--bottom gold-gradient"></div>
    <div class="brand-dot"></div>
    <h1 class="brand-name">VELMORA<br>BOTANICA</h1>
    <h2 class="product-name">MANUKA<br>HONEY</h2>
    <svg class="grade-badge" viewBox="0 0 46 29" aria-label="Grade rating badge">
      <defs>
        <linearGradient id="badgeGold" x1="0" x2="1">
          <stop offset="0" stop-color="#b8750c"/>
          <stop offset="0.5" stop-color="#f5d37a"/>
          <stop offset="1" stop-color="#b8750c"/>
        </linearGradient>
      </defs>
      <polygon points="7,1 39,1 45,14.5 39,28 7,28 1,14.5" fill="none" stroke="url(#badgeGold)" stroke-width="1.5"/>
      <polygon points="9,4 37,4 42,14.5 37,25 9,25 4,14.5" fill="none" stroke="url(#badgeGold)" stroke-width="0.8"/>
    </svg>
    <p class="origin">HARVESTED IN NEW ZEALAND</p>
    <p class="net-weight">250g (8.8oz) NET Wt.</p>
  </section>

</main>
</body>
</html>
```